"The Craft of Patron Care," fourth edition cover design

Later this year, my publisher, Harold Penmarsh & Daughters, will issue a fourth, substantially revised edition of "The Craft of Patron Care," following the 2016 publication of the third edition and the second and first versions that were issued earlier.

To distinguish this new edition from previous ones, I need a cover design that visually connects and is consistent with what has preceded it, while signaling this is a new and different, worthy of prospective readers/buyers’ attention.

Attached are three different verbal approaches to the new cover; these are NOT MEANT to serve as actual designs, but rather will give you a sense of how language is to be deployed:

The first emphasizes “ART” as the key visual word in the book title;
The second emphasizes “CLIENT SERVICE” as the key visual words in the book title; and,
The third emphasizes just the word "CLIENT" in the book title.

A top-of-the-page is a pre-head that applies to all three versions:
“6 TIMELESS PRINCIPLES FOR ADVERTISING & MARKETING PRO’s
IN AN AI WORLD"

There's a mid-page sub-head for all three versions:
“THE CLASSIC GUIDE,” followed by
“FOURTH EDITION BY GERALD ASHCOMBE

And there's a one-line, bottom-of-the-page designation:
“Foreword by Mae Dunford, Global Executive Creative Director, Starbolt"

The pallette for the previously published third edition was black with red as an accent color on a field of white; I've attached a sample for reference, so you can see how it was executed. For this new fourth edition, I'd like to change the accent color from red to either Wedgewood blue, or British racing green, or an alternative that is assertive and color saturated -- think of primary colors -- that contrast sufficiently with the base of black. As an alternative, you can consider a cover that used either Wedgewood blue, British racing green, or another possibility as a full-bleed field, with copy content either revered out or surprinted.

Lastly, while the new cover largely is meant to be typographically driven, if you can come up with a visual metaphor that illustrates and builds on the book's title, that would be very helpful. By way of reference, the third edition's book cover attempted to do this by introducing a visual element at the end of the book's title that's meant to represent an artist's paint splatter (although I admit it didn't work as well as it should).

Target Market(s)

Prospective purchasers of the book who might discover copies at a bookstore, but more likely will encounter it through online distributors such as Riverdex, Hartwell & Pike, and Tindall’s.

Industry/Entity Type

Advertising and marketing

Font styles to use
Serif
Sans Serif
Other font styles liked:
• A mix of serif and san-serif typefaces is okay. for the examples I shared, I relieid on "Arial Rounded Bold" but you need not be weeded to this. If you opt to mix in a serif font, I am partial to Cambria as a typeface.

Requirements
Must have
• To achieve the goal of being “connected with but distinct” from previous editions, the new cover should be:  Largely typographic, but displaying a color palette different from the previous editions’ black-plus-red-accent on a canvas of white.  Any new accent color selected for use should be vibrant, strong, and highly saturated; think “British racing green,” “Wedgewood blue,” or their equivalents.  In addition to a powerful, “billboard” approach to type and color, consider other visual metaphors that are likely to engage the readers. The winning cover design will stand out from other books, while connecting with the previously published third edition.
Nice to have
• If you can find way to illustrate the book's title through a visual metaphor, that would be ideal.a
Should not have
• Anything that is frivolous or non-sensical

```html
<!DOCTYPE html>
<html lang="en">
<head>
<meta charset="utf-8">
<title>The Craft of Patron Care — Fourth Edition Cover</title>
<link rel="stylesheet" href="https://fonts.googleapis.com/css2?family=Anton&family=Montserrat:wght@500;600;700&family=Oswald:wght@300;700&family=Playfair+Display:ital,wght@1,700&display=swap">
<style>
  :root {
    --backdrop: #d9d9d9;
    --paper: #ffffff;
    --ink: #231f20;
    --racing-green: #015c03;
  }
  html, body {
    margin: 0;
    padding: 0;
    width: 1200px;
    height: 1200px;
    overflow: hidden;
    background: var(--backdrop);
  }
  .cover-stage {
    display: block;
    width: 1200px;
    height: 1200px;
  }
  .cover-sheet { fill: var(--paper); }
  .prehead {
    font-family: "Montserrat", sans-serif;
    font-weight: 500;
    font-size: 21px;
    fill: var(--ink);
  }
  .prehead .accent { fill: var(--racing-green); font-weight: 700; }
  .title-lead {
    font-family: "Playfair Display", serif;
    font-style: italic;
    font-weight: 700;
    font-size: 50px;
    letter-spacing: -1px;
    fill: var(--ink);
  }
  .title-rule { fill: var(--racing-green); }
  .title-main {
    font-family: "Anton", sans-serif;
    fill: var(--racing-green);
  }
  .subhead {
    font-family: "Montserrat", sans-serif;
    font-weight: 600;
    font-size: 40px;
    letter-spacing: 2px;
    fill: var(--ink);
  }
  .edition {
    font-family: "Montserrat", sans-serif;
    font-weight: 600;
    font-size: 40px;
    letter-spacing: -1.5px;
    fill: var(--racing-green);
  }
  .author {
    font-family: "Oswald", sans-serif;
    font-weight: 700;
    font-size: 58px;
    letter-spacing: 1px;
    fill: var(--racing-green);
  }
  .foreword {
    font-family: "Oswald", sans-serif;
    font-weight: 300;
    font-size: 23px;
    fill: var(--ink);
  }
  .publisher {
    font-family: "Montserrat", sans-serif;
    font-weight: 700;
    font-size: 13px;
    letter-spacing: 0.5px;
    fill: var(--ink);
  }
</style>
</head>
<body>
<svg class="cover-stage" viewBox="0 0 1200 1200" xmlns="http://www.w3.org/2000/svg" role="img" aria-label="Cover of The Craft of Patron Care, fourth edition, by Gerald Ashcombe">
  <rect class="cover-sheet" x="273" y="109" width="654" height="981"/>

  <text class="prehead" x="598" y="200" text-anchor="middle">6 TIMELESS PRINCIPLES FOR ADVERTISING &amp;</text>
  <text class="prehead" x="598" y="227" text-anchor="middle">MARKETING PRO’s IN AN <tspan class="accent">AI WORLD</tspan></text>

  <polygon class="title-rule" points="324,320 436,317 436,323"/>
  <polygon class="title-rule" points="764,317 879,320 764,323"/>
  <text class="title-lead" x="600" y="329" text-anchor="middle" textLength="308" lengthAdjust="spacingAndGlyphs">THE CRAFT OF</text>

  <text class="title-main" x="328" y="535" font-size="218" textLength="552" lengthAdjust="spacingAndGlyphs">PATRON</text>
  <text class="title-main" x="324" y="724" font-size="196" textLength="556" lengthAdjust="spacingAndGlyphs">CARE</text>

  <polygon class="title-rule" points="328,742 603,739 879,742 603,745"/>

  <text class="subhead" x="600" y="837" text-anchor="middle" textLength="386" lengthAdjust="spacingAndGlyphs">THE CLASSIC GUIDE</text>
  <text class="edition" x="597" y="885" text-anchor="middle" textLength="324" lengthAdjust="spacingAndGlyphs">FOURTH EDITION</text>

  <text class="author" x="599" y="977" text-anchor="middle" textLength="354" lengthAdjust="spacingAndGlyphs">GERALD ASHCOMBE</text>
  <text class="foreword" x="599" y="1008" text-anchor="middle" textLength="538" lengthAdjust="spacingAndGlyphs">Foreword by Mae Dunford, Global Executive Creative Director, Starbolt</text>

  <text class="publisher" x="884" y="1059" text-anchor="end">HAROLD PENMARSH &amp; DAUGHTERS</text>
</svg>
</body>
</html>
```